Business Card and Letterhead for Vantage Psychology

We need a business card design and letterhead to use for our Psychology firm that specializes in psychoeducational assessments and individual therapy. Our motto is Purpose-Driven Assessments, Meaning-Centered Therapy.Our contact information is as follows:
Vantage Psychology
The Marwick Block - 6127-48St.
Box 2716 Elmridge, KV
T2K 3M8
t 403.555.0148 (VANT)
f 403.555.0172
www.vantagepsychology-example.ca
The business card will be used for two different psychologists so I can supply names nearer to completion. We prefer clean, uncluttered looks.

Target Market(s)

Clients, Educators

Font styles to use
Sans Serif

Colors

Designer to choose colors to be used in the design.

Requirements
Must have
• All relevant contact info, logo, some "white" space.
Nice to have
• It would be nice to see letterhead options that have the logo on the top of the page but also options that have it on the side. I think top of the page is probably our preference.
Should not have
• Too much clutter!

```html
<!DOCTYPE html>
<html lang="en">
<head>
<meta charset="utf-8">
<title>Vantage Psychology – Business Cards</title>
<link href="https://fonts.googleapis.com/css2?family=Arimo:wght@400;700&display=swap" rel="stylesheet">
<style>
  :root {
    --page-bg: #e2e2e3;
    --card-white: #f3f3f3;
    --brand-blue: #48b3d4;
    --brand-orange: #e9a046;
    --ink: #222222;
    --ink-soft: #3a3a3a;
    --url-light: #f6dcb8;
    --white: #ffffff;
  }
  * { margin: 0; padding: 0; box-sizing: border-box; }
  html, body {
    width: 1200px; height: 879px; overflow: hidden;
    background: var(--page-bg);
    font-family: "Arimo", Arial, sans-serif;
  }
  .card {
    position: absolute;
    width: 354px; height: 203px;
    overflow: hidden;
  }
  .card--front { background: var(--card-white); }
  .card--back-blue { background: var(--brand-blue); }
  .card--back-orange { background: var(--brand-orange); }

  .row-1 { top: 197px; }
  .row-2 { top: 478px; }
  .col-front { left: 239px; }
  .col-back { left: 610px; }

  .edge-tab {
    position: absolute; left: 0; top: 110px;
    width: 13px; height: 69px;
    background: var(--brand-blue);
  }
  .brand-mark {
    position: absolute; left: 83px; top: 34px;
    width: 40px; height: 40px; border-radius: 50%;
    background: var(--brand-blue);
  }
  .brand-name {
    position: absolute; left: 40px; top: 74px;
    font-size: 10px; line-height: 12px; font-weight: 700;
    text-transform: uppercase;
    color: var(--brand-blue);
    white-space: nowrap;
  }

  .contact { color: var(--ink); font-size: 8.5px; line-height: 10px; white-space: nowrap; }
  .contact__name,
  .contact__role,
  .contact__line { position: absolute; left: 41px; }
  .contact__name {
    top: 102px;
    color: var(--brand-orange);
    font-size: 11.5px; font-weight: 700; line-height: 13px;
  }
  .contact__role  { top: 117px; }
  .contact__line--street { top: 134px; }
  .contact__line--town   { top: 144px; }
  .contact__line--tel    { top: 159px; }
  .contact__line--fax    { top: 169px; }
  .label { color: var(--brand-orange); }
  .vanity { color: var(--brand-blue); }

  .split-disc {
    position: absolute; top: 55px;
    width: 123px; height: 123px; border-radius: 50%;
  }
  .card--front .split-disc { left: 297px; background: var(--brand-blue); }
  .card--back-blue .split-disc { left: -74px; background: var(--white); }
  .card--back-orange .split-disc { left: -74px; background: var(--brand-blue); }

  .back-title {
    position: absolute; left: 79px; top: 95px; width: 252px;
    text-align: center;
    font-size: 17px; line-height: 20px; font-weight: 700; letter-spacing: 0.4px;
    text-transform: uppercase; white-space: nowrap;
    color: var(--white);
  }
  .back-url {
    position: absolute; left: 70px; top: 116px; width: 270px;
    text-align: center; font-size: 8.5px; line-height: 10px; white-space: nowrap;
  }
  .back-url b { font-weight: 700; }
  .card--back-blue .back-url { color: var(--ink-soft); }
  .card--back-orange .back-url { color: var(--url-light); }
</style>
</head>
<body>

  <section class="card card--front row-1 col-front">
    <div class="edge-tab"></div>
    <div class="brand-mark"></div>
    <div class="brand-name">Vantage Psychology</div>
    <div class="contact">
      <div class="contact__name">Daren Kovalsky</div>
      <div class="contact__role">CEO</div>
      <div class="contact__line contact__line--street">The Marwick Block - 6127-48St.</div>
      <div class="contact__line contact__line--town">Box 2716 Elmridge, KV T2K 3M8</div>
      <div class="contact__line contact__line--tel"><span class="label">t</span> 403.555.0148 <span class="vanity">(VANT)</span></div>
      <div class="contact__line contact__line--fax"><span class="label">f</span> 403.555.0172</div>
    </div>
    <div class="split-disc"></div>
  </section>

  <section class="card card--back-blue row-1 col-back">
    <div class="split-disc"></div>
    <div class="back-title">Vantage Psychology</div>
    <div class="back-url">www.<b>vantagepsychology-example</b>.ca</div>
  </section>

  <section class="card card--front row-2 col-front">
    <div class="brand-mark"></div>
    <div class="brand-name">Vantage Psychology</div>
    <div class="contact">
      <div class="contact__name">Daren Kovalsky</div>
      <div class="contact__role">CEO</div>
      <div class="contact__line contact__line--street">The Marwick Block - 6127-48St.</div>
      <div class="contact__line contact__line--town">Box 2716 Elmridge, KV T2K 3M8</div>
      <div class="contact__line contact__line--tel"><span class="label">t</span> 403.555.0148 <span class="vanity">(VANT)</span></div>
      <div class="contact__line contact__line--fax"><span class="label">f</span> 403.555.0172</div>
    </div>
    <div class="split-disc"></div>
  </section>

  <section class="card card--back-orange row-2 col-back">
    <div class="split-disc"></div>
    <div class="back-title">Vantage Psychology</div>
    <div class="back-url">www.<b>vantagepsychology-example</b>.ca</div>
  </section>

</body>
</html>
```